Specialist Technical Theatre service for schools

The task is to design a brochure (A5, 4 pages) for mailing to secondary/high school heads and drama departments to sell them our services as Technical Theatre and Drama professionals who can help them to offer elements of a curriculum that they do not currently offer as well as raise the technical standards of their school productions.
Please find a document attached which outlines the content for the brochure. Please read the document first so that you understand our aims. The text highlighted in yellow takes priority - the text highlighted in blue could be used if there is space.
Photos which may be used available on https://www.pictaro.com/photos/ben_tovey/ (please do not use watermarked nordel images).
Logo is attached (two variants) - one of which should appear somewhere on the design. Website address is www.cresthalltheatre.co.uk and email is info@cresthalltheatre.co.uk
Target Market(s)
Theatre and Drama teachers in Secondary/High schools
Headteachers of Secondary/High Schools
Industry/Entity Type
Education
Look and feel

```html
<!DOCTYPE html>
<html lang="en">
<head>
<meta charset="utf-8">
<title>School Technical Theatre – Brochure Spreads</title>
<link href="https://fonts.googleapis.com/css2?family=Cinzel:wght@600;700&family=Open+Sans:wght@400;600;700&display=swap" rel="stylesheet">
<style>
  :root{
    --backdrop:#3b3b3d;
    --navy:#17244a;
    --navy-deep:#0e1733;
    --gold:#c9952e;
    --gold-light:#e8c06a;
    --paper:#ffffff;
    --ink:#3a3f4c;
    --stage-purple:#4b2a78;
    --stage-blue:#2a4fa0;
    --stone:#b9b2a4;
    --badge:#d8dbe3;
  }
  *{box-sizing:border-box;margin:0;padding:0}
  html,body{width:900px;height:1200px;overflow:hidden;background:var(--backdrop)}
  body{font-family:"Open Sans",Arial,sans-serif;color:var(--ink);position:relative}

  .page{position:absolute;width:410px;height:570px;background:var(--paper);overflow:hidden;box-shadow:0 6px 18px rgba(0,0,0,.45)}
  .page--cover{left:30px;top:25px}
  .page--inside-left{left:460px;top:25px}
  .page--inside-right{left:30px;top:615px}
  .page--back{left:460px;top:615px}

  .photo{position:absolute}
  .swoosh{position:absolute;left:0;width:410px}
  .band{position:absolute;left:0;width:100%}

  .logo{position:absolute;left:50%;transform:translateX(-50%);display:flex;align-items:center;gap:6px;background:var(--navy);padding:7px 10px;border:1px solid var(--gold);z-index:3;white-space:nowrap}
  .logo__dot{width:9px;height:9px;border-radius:50%;background:var(--gold)}
  .logo__name{font-weight:700;font-size:10px;letter-spacing:1.5px;color:#fff}

  .footer{position:absolute;left:0;bottom:0;width:100%;height:52px;background:linear-gradient(180deg,var(--navy),var(--navy-deep));display:flex;align-items:center;justify-content:center;gap:18px}
  .footer__text{font-size:10px;font-weight:600;color:#fff;letter-spacing:.5px;position:relative;top:8px}

  .small{font-size:8px;line-height:1.55}

  .cover__title{position:absolute;top:236px;left:0;width:100%;text-align:center;font-family:"Cinzel",Georgia,serif;color:var(--gold);font-weight:700;line-height:1.15}
  .cover__title span{display:block}
  .cover__title .l1{font-size:19px}
  .cover__title .l2{font-size:15px}
  .cover__intro{position:absolute;top:290px;left:30px;right:30px;text-align:center}

  .bullets{list-style:none}
  .bullets li{position:relative;padding-left:11px;margin-bottom:8px}
  .bullets li::before{content:"";position:absolute;left:0;top:4px;width:5px;height:5px;background:var(--gold)}
</style>
</head>
<body>

<section class="page page--cover">
  <div class="photo" style="left:0;top:0;width:410px;height:210px;background:radial-gradient(ellipse at 50% 40%,#d9a3e6 0%,var(--stage-purple) 45%,#160d2e 100%)" role="img" aria-label="Performer on a lit theatre stage with purple and blue lighting"></div>
  <div class="logo" style="top:172px"><span class="logo__dot"></span><span class="logo__name">CRESTHALL</span></div>
  <svg class="swoosh" style="top:186px" height="48" viewBox="0 0 410 48" aria-hidden="true">
    <path d="M0 18 Q205 48 410 10 L410 48 L0 48 Z" fill="#fff"/>
    <path d="M0 18 Q205 46 410 10 L410 16 Q205 52 0 24 Z" fill="var(--gold)"/>
  </svg>
  <h1 class="cover__title"><span class="l1">School Technical Theatre</span><span class="l2">Support by Industry Professionals</span></h1>
  <p class="cover__intro small">We are a team of working theatre technicians and drama practitioners who bring industry skills into schools, helping students and staff build confidence in lighting, sound, stage management and production design for every performance.</p>
  <div class="photo" style="left:0;top:356px;width:205px;height:165px;background:linear-gradient(160deg,#3b6fd1,#1b1f5c 60%,#e0a040)" role="img" aria-label="Concert stage with bright lighting rig and audience"></div>
  <div class="photo" style="left:205px;top:356px;width:205px;height:165px;background:linear-gradient(180deg,#1a2a5a,#3a4f8a 55%,#d79a45)" role="img" aria-label="Theatre building lit up at night"></div>
  <svg class="swoosh" style="top:496px" height="30" viewBox="0 0 410 30" aria-hidden="true">
    <path d="M0 10 Q205 34 410 6 L410 30 L0 30 Z" fill="var(--navy)"/>
    <path d="M0 10 Q205 32 410 6 L410 11 Q205 38 0 15 Z" fill="var(--gold)"/>
  </svg>
  <footer class="footer"><span class="footer__text">www.cresthalltheatre.co.uk</span></footer>
</section>

<section class="page page--inside-left">
  <div class="band" style="top:0;height:62px;background:linear-gradient(180deg,var(--navy-deep),var(--navy))"></div>
  <div class="logo" style="top:14px"><span class="logo__dot"></span><span class="logo__name">CRESTHALL</span></div>
  <svg class="swoosh" style="top:50px" height="24" viewBox="0 0 410 24" aria-hidden="true">
    <path d="M0 4 Q205 26 410 2 L410 8 Q205 32 0 10 Z" fill="var(--gold)"/>
  </svg>
  <div class="small" style="position:absolute;top:82px;left:24px;right:24px;text-align:center">
    <p>Our specialist staff work alongside your drama department to deliver practical technical theatre teaching, support exam coursework and raise the standard of school productions from first rehearsal to final curtain.</p>
    <p style="margin-top:5px;font-weight:700;color:var(--navy)">Call us to arrange a free consultation for your school.</p>
  </div>
  <div class="photo" style="left:0;top:152px;width:410px;height:190px;background:linear-gradient(180deg,#8fb3da 0%,#c9c3b6 45%,var(--stone) 70%,#6f6a62 100%)" role="img" aria-label="Crowd gathered outside a large classical building"></div>
  <div class="band" style="top:342px;height:4px;background:var(--gold)"></div>
  <div class="small" style="position:absolute;top:366px;left:24px;right:24px;display:flex;gap:20px">
    <ul class="bullets" style="flex:1">
      <li>Lighting design and operation</li>
      <li>Sound design and mixing</li>
      <li>Stage management skills</li>
      <li>Set and prop construction</li>
    </ul>
    <ul class="bullets" style="flex:1">
      <li>Technical theatre workshops</li>
      <li>Exam coursework support</li>
      <li>Production week assistance</li>
      <li>Staff training sessions</li>
    </ul>
  </div>
  <svg class="swoosh" style="top:496px" height="30" viewBox="0 0 410 30" aria-hidden="true">
    <path d="M0 10 Q205 34 410 6 L410 30 L0 30 Z" fill="var(--navy)"/>
    <path d="M0 10 Q205 32 410 6 L410 11 Q205 38 0 15 Z" fill="var(--gold)"/>
  </svg>
  <footer class="footer"></footer>
</section>

<section class="page page--inside-right">
  <div class="photo" style="left:0;top:0;width:140px;height:200px;background:linear-gradient(170deg,#e06a2a,#7a1f3c 60%,#1c1030)" role="img" aria-label="Actor in costume under warm stage lights"></div>
  <div class="photo" style="left:140px;top:0;width:270px;height:200px;background:radial-gradient(ellipse at 60% 30%,#9fc4ff,var(--stage-blue) 50%,#0d1233)" role="img" aria-label="Audience in front of a lit concert stage"></div>
  <div class="logo" style="top:14px"><span class="logo__dot"></span><span class="logo__name">CRESTHALL</span></div>
  <div class="band" style="top:200px;height:58px;background:var(--navy);border-top:3px solid var(--gold);border-bottom:3px solid var(--gold);display:flex;align-items:center;justify-content:center;padding:0 36px">
    <p style="font-size:8.5px;font-weight:600;color:#fff;text-align:center;line-height:1.5">Give your students real industry experience and the confidence to run their own shows.</p>
  </div>
  <div class="small" style="position:absolute;top:280px;left:24px;right:24px;display:flex;gap:20px">
    <ul class="bullets" style="flex:1">
      <li>Hands-on sessions led by professional technicians in your own school hall.</li>
      <li>Training on the equipment you already own, safely and correctly.</li>
      <li>Support for GCSE and A Level technical theatre options.</li>
      <li>Clear written guides for students to keep after each visit.</li>
    </ul>
    <ul class="bullets" style="flex:1">
      <li>Full production support during show week and dress rehearsals.</li>
      <li>Advice on new lighting and sound equipment purchases.</li>
      <li>Flexible packages to suit every school budget.</li>
      <li>Follow-up support by phone and email between visits.</li>
    </ul>
  </div>
  <svg class="swoosh" style="top:496px" height="30" viewBox="0 0 410 30" aria-hidden="true">
    <path d="M0 10 Q205 34 410 6 L410 30 L0 30 Z" fill="var(--navy)"/>
    <path d="M0 10 Q205 32 410 6 L410 11 Q205 38 0 15 Z" fill="var(--gold)"/>
  </svg>
  <footer class="footer"><span class="footer__text">www.cresthalltheatre.co.uk</span></footer>
</section>

<section class="page page--back">
  <div class="band" style="top:0;height:62px;background:linear-gradient(180deg,var(--navy-deep),var(--navy))"></div>
  <div class="logo" style="top:14px"><span class="logo__dot"></span><span class="logo__name">CRESTHALL</span></div>
  <div class="band" style="top:62px;height:74px;background:linear-gradient(180deg,var(--gold-light),var(--gold));display:flex;align-items:center;justify-content:center;padding:0 40px">
    <p style="font-size:9px;font-weight:700;color:#fff;text-align:center;line-height:1.5">We can support your school in as many ways as you need, from one workshop to a full year.</p>
  </div>
  <div class="small" style="position:absolute;top:156px;left:28px;right:28px;text-align:center">
    <p style="margin-bottom:10px">Our team has worked on touring shows, large city venues and festivals, and we bring that experience to every school we visit.</p>
    <p style="margin-bottom:10px">Every session is planned with your staff so that it fits your curriculum, your timetable and your students.</p>
    <p style="margin-bottom:10px">Sessions can run in the day, after school or during holidays, and all staff hold full safeguarding checks.</p>
    <p style="margin-bottom:14px">We also offer taster days so your students can try each technical role before choosing a course.</p>
    <p style="font-weight:700;color:var(--navy);font-size:8.5px">Get in touch today to book your free visit.</p>
  </div>
  <div style="position:absolute;top:430px;left:40px;right:40px;display:flex;justify-content:space-between;align-items:center">
    <span style="width:50px;height:26px;background:var(--badge);border-radius:3px"></span>
    <span style="width:34px;height:34px;background:var(--badge);border-radius:50%"></span>
    <span style="width:50px;height:26px;background:var(--badge);border-radius:3px"></span>
    <span style="width:34px;height:34px;background:var(--badge);border-radius:50%"></span>
    <span style="width:50px;height:26px;background:var(--badge);border-radius:3px"></span>
  </div>
  <svg class="swoosh" style="top:496px" height="30" viewBox="0 0 410 30" aria-hidden="true">
    <path d="M0 10 Q205 34 410 6 L410 30 L0 30 Z" fill="var(--navy)"/>
    <path d="M0 10 Q205 32 410 6 L410 11 Q205 38 0 15 Z" fill="var(--gold)"/>
  </svg>
  <footer class="footer"><span class="footer__text">www.cresthalltheatre.co.uk</span><span class="footer__text">info@cresthalltheatre.co.uk</span></footer>
</section>

</body>
</html>
```